Criação de Cartao de Visita para Vigor & Equilíbrio
" Venda de Suplementos Alimentares/Nutricionais, principalmente via whatsapp e facebook, fazemos entregas e aceitamos cartões. Ainda não possuimos loja física. Cobrimos qualquer oferta de site ou loja nacional. "

```html
<!DOCTYPE html>
<html lang="pt-BR">
<head>
<meta charset="UTF-8">
<title>Vigor &amp; Equilíbrio — Cartão de Visita</title>
<link href="https://fonts.googleapis.com/css2?family=Montserrat:ital,wght@0,400;0,600;0,800;1,800&display=swap" rel="stylesheet">
<style>
  :root {
    --bg: #e9eaec;
    --black: #0c0c0c;
    --black-soft: #1f1f1f;
    --gold: #f0a81c;
    --gold-deep: #d98b0c;
    --white: #ffffff;
    --ink: #1a1a1a;
    --grey: #555555;
  }
  * { margin: 0; padding: 0; box-sizing: border-box; }
  html, body { width: 1200px; height: 1200px; overflow: hidden; }
  body {
    background: var(--bg);
    font-family: "Montserrat", Arial, sans-serif;
    display: flex;
    flex-direction: column;
    align-items: center;
    justify-content: center;
    gap: 70px;
  }
  .card {
    width: 900px;
    height: 500px;
    position: relative;
    overflow: hidden;
    box-shadow: 0 18px 40px rgba(0,0,0,0.18);
  }
  .card-front {
    background: linear-gradient(135deg, var(--black-soft) 0%, var(--black) 55%, #050505 100%);
    display: flex;
    align-items: center;
    justify-content: center;
  }
  .card-front::after {
    content: "";
    position: absolute;
    left: 0; right: 0; bottom: 0;
    height: 10px;
    background: linear-gradient(90deg, var(--gold-deep), var(--gold));
  }
  .brand {
    display: flex;
    flex-direction: column;
    align-items: center;
    gap: 26px;
  }
  .brand-mark {
    width: 110px;
    height: 110px;
    border-radius: 50%;
    background: var(--gold);
  }
  .brand-name {
    font-weight: 800;
    font-size: 54px;
    letter-spacing: 0.5px;
    color: var(--gold);
  }
  .card-back {
    background: var(--white);
    display: flex;
    align-items: center;
    padding: 0 60px 0 70px;
  }
  .card-back::after {
    content: "";
    position: absolute;
    left: 0; right: 0; bottom: 0;
    height: 18px;
    background: linear-gradient(90deg, var(--gold-deep), var(--gold));
  }
  .card-back .brand { gap: 20px; width: 380px; }
  .card-back .brand-mark { width: 90px; height: 90px; }
  .card-back .brand-name { font-size: 34px; color: var(--gold-deep); }
  .contact {
    margin-left: auto;
    text-align: right;
  }
  .person-name {
    font-weight: 800;
    font-size: 24px;
    color: var(--ink);
    letter-spacing: 1px;
  }
  .person-role {
    font-size: 15px;
    color: var(--grey);
    margin-bottom: 30px;
  }
  .contact-list { list-style: none; }
  .contact-item {
    display: flex;
    align-items: center;
    justify-content: flex-end;
    gap: 14px;
    font-size: 16px;
    font-weight: 600;
    color: var(--ink);
    margin-bottom: 12px;
  }
  .contact-icon {
    width: 26px;
    height: 26px;
    background: var(--gold);
    display: flex;
    align-items: center;
    justify-content: center;
    flex-shrink: 0;
  }
  .contact-icon svg { width: 16px; height: 16px; }
  .address { line-height: 1.35; }
</style>
</head>
<body>
  <section class="card card-front">
    <div class="brand">
      <span class="brand-mark"></span>
      <span class="brand-name">Vigor &amp; Equilíbrio</span>
    </div>
  </section>

  <section class="card card-back">
    <div class="brand">
      <span class="brand-mark"></span>
      <span class="brand-name">Vigor &amp; Equilíbrio</span>
    </div>
    <div class="contact">
      <p class="person-name">NOME SOBRENOME</p>
      <p class="person-role">Função</p>
      <ul class="contact-list">
        <li class="contact-item">contato@vigorequilibrio.com.br
          <span class="contact-icon"><svg viewBox="0 0 16 16"><rect x="2" y="4" width="12" height="8" fill="none" stroke="#fff" stroke-width="1.6"/><path d="M2 4l6 5 6-5" fill="none" stroke="#fff" stroke-width="1.6"/></svg></span>
        </li>
        <li class="contact-item">www.vigorequilibrio.com.br
          <span class="contact-icon"><svg viewBox="0 0 16 16"><circle cx="8" cy="8" r="6" fill="none" stroke="#fff" stroke-width="1.5"/><ellipse cx="8" cy="8" rx="2.6" ry="6" fill="none" stroke="#fff" stroke-width="1.2"/><path d="M2 8h12" stroke="#fff" stroke-width="1.2"/></svg></span>
        </li>
        <li class="contact-item">(11) 98765-4321
          <span class="contact-icon"><svg viewBox="0 0 16 16"><path d="M4 2h3l1 3-2 1.2a8 8 0 0 0 3.8 3.8L11 8l3 1v3a2 2 0 0 1-2 2A10 10 0 0 1 2 4a2 2 0 0 1 2-2z" fill="#fff"/></svg></span>
        </li>
        <li class="contact-item">(11) 98765-4321
          <span class="contact-icon"><svg viewBox="0 0 16 16"><rect x="4.5" y="1.5" width="7" height="13" rx="1.5" fill="none" stroke="#fff" stroke-width="1.5"/><circle cx="8" cy="12" r="0.9" fill="#fff"/></svg></span>
        </li>
        <li class="contact-item"><span class="address">Endereço Completo, 000 Bairro<br>Cidade/Estado</span>
          <span class="contact-icon"><svg viewBox="0 0 16 16"><path d="M8 15s-5-5.2-5-8.5a5 5 0 0 1 10 0C13 9.8 8 15 8 15z" fill="#fff"/><circle cx="8" cy="6.5" r="1.8" fill="#f0a81c"/></svg></span>
        </li>
      </ul>
    </div>
  </section>
</body>
</html>
```